Election features for a political website

The Evening Lantern (www.eveninglantern.co.uk)
Web banner designs
Please have a look at The Evening Lantern website (www.eveninglantern.co.uk). We are seeking to add an advertising style banner at the top of every page and post. It will run right across the page (1024 pixels) and be in the region of 200 pixels vertically. (Please advise on what looks best size wise.
The banner will be a slider, operated in a similar way to the current homepage slider. There will be four items on the slider, and so we need four designs that match the aesthetic feel of the website. Each slider will link through to posts on the website.
1.
Headline: OUR CANDIDATE OF THE DAY
Space for a name, head and shoulders picture of the person to be dropped in and a one line reason. This will need to be in an editable format as this image will be changed each day for one month.
2.
Headline: HERO OF THE DAY
Space for name and a one line reason. This will need to be in an editable format as this image will be changed each day for one month.
3.
Headline: VILLAIN OF THE DAY
Space for name of the person to be dropped in and a one line reason. This will need to be in an editable format as this image will be changed each day for one month.
4.
Headline: TEL Poll – [Date]
If the election was today, who would you vote for?
Clickable options:
Harbourites
Meridan
Tallow Assembly
Pomo
Quill
Other
Can a poll widget be added to the banner? We would like this poll to reset each day and then pool the results into a graph day by day over a one month period.
Reason: Payment is now guaranteed. We would like to see more options.

```html
<!DOCTYPE html>
<html lang="en">
<head>
<meta charset="utf-8">
<title>Hero of the Day – The Evening Lantern banner</title>
<link rel="stylesheet" href="https://fonts.googleapis.com/css2?family=Tinos:wght@400;700&family=Arimo:wght@700&display=swap">
<style>
  :root {
    --navy: #02528a;
    --band: #1e6595;
    --rule: #0a80cc;
    --ink-light: #ffffff;
    --note: #1f5c8e;
    --photo-light: #f4f4f4;
    --photo-dark: #3a3a3a;
  }
  html, body {
    margin: 0;
    padding: 0;
    width: 1200px;
    height: 420px;
    overflow: hidden;
    background: #ffffff;
  }
  .canvas {
    position: relative;
    width: 1200px;
    height: 420px;
  }
  .banner {
    position: absolute;
    left: 10px;
    top: 10px;
    width: 1023px;
    height: 400px;
    background: var(--navy);
  }
  .banner__rule {
    position: absolute;
    left: 0;
    width: 522px;
    height: 6px;
    background: var(--rule);
  }
  .banner__rule--top { top: 55px; }
  .banner__rule--bottom { top: 240px; }
  .banner__headline-band {
    position: absolute;
    left: 0;
    top: 61px;
    width: 522px;
    height: 179px;
    background: var(--band);
  }
  .banner__headline {
    position: absolute;
    left: 41px;
    top: 124px;
    margin: 0;
    font-family: "Tinos", "Times New Roman", serif;
    font-weight: 700;
    font-size: 41px;
    letter-spacing: 0.3px;
    line-height: 1;
    color: var(--ink-light);
  }
  .banner__name {
    position: absolute;
    left: 41px;
    top: 285px;
    margin: 0;
    font-family: "Arimo", Arial, sans-serif;
    font-weight: 700;
    font-size: 47px;
    line-height: 1;
    color: var(--ink-light);
  }
  .banner__portrait {
    position: absolute;
    left: 522px;
    top: 12px;
    width: 490px;
    height: 376px;
    background:
      radial-gradient(ellipse 45% 60% at 42% 95%, var(--photo-dark) 0%, rgba(58,58,58,0.6) 55%, rgba(58,58,58,0) 100%),
      linear-gradient(180deg, var(--photo-light) 0%, #ffffff 100%);
  }
  .size-note {
    position: absolute;
    left: 1082px;
    top: 175px;
    margin: 0;
    font-family: "Tinos", "Times New Roman", serif;
    font-size: 16px;
    line-height: 29px;
    color: var(--note);
  }
</style>
</head>
<body>
<div class="canvas">
  <section class="banner">
    <div class="banner__headline-band"></div>
    <div class="banner__rule banner__rule--top"></div>
    <div class="banner__rule banner__rule--bottom"></div>
    <h1 class="banner__headline">HERO OF THE DAY</h1>
    <p class="banner__name">ALDEN MARSH</p>
    <div class="banner__portrait" role="img" aria-label="Black and white head and shoulders photo of the day's hero, cheering with fists raised"></div>
  </section>
  <p class="size-note">BANNER<br>SIZE<br>1024x400</p>
</div>
</body>
</html>
```